Professional & attention grabbing.

A business card design, front and back. I already have a logo I will attach, but I am open to something new as well.
Things to include:
Name:
Title:
Phone:
Email:
Wanting something that is professional but attention grabbing.
Also we do a lot of work using drones on natural gas pipelines (leading the future)if you want to include any of that. I'm open to ideas.
Target Market(s)
Natural gas transmission industry / greenhouse gas mitigation industry
Industry/Entity Type
Business
Contact Information for Business Card
All details have been conveyed above.
Colors
Designer to choose colors to be used in the design.
Look and feel
Each slider illustrates characteristics of the customer's brand and the style your logo design should communicate.

```html
<!DOCTYPE html>
<html lang="en">
<head>
<meta charset="utf-8">
<title>KV Field Surveys — Business Card</title>
<link rel="stylesheet" href="https://fonts.googleapis.com/css2?family=Open+Sans:wght@400;600;700&display=swap">
<style>
  :root {
    --backdrop: #dedad5;
    --card-grey: #e6e7e8;
    --card-white: #ffffff;
    --panel-dark: #3a3a3c;
    --accent-red: #c0222b;
    --text-dark: #2f2f31;
    --text-light: #ffffff;
  }
  * { margin: 0; padding: 0; box-sizing: border-box; }
  html, body {
    width: 1200px;
    height: 1135px;
    overflow: hidden;
    background: var(--backdrop);
    font-family: "Open Sans", Arial, sans-serif;
  }
  .card {
    position: absolute;
    left: 237px;
    width: 679px;
    height: 405px;
    box-shadow: 0 14px 28px rgba(0,0,0,0.25);
  }
  .card--front { top: 90px; }
  .card--back { top: 625px; }
  .card__art { position: absolute; inset: 0; width: 100%; height: 100%; display: block; }

  .brand {
    position: absolute;
    display: flex;
    align-items: center;
    color: var(--text-dark);
    font-weight: 700;
  }
  .brand__square { background: var(--accent-red); flex: none; }
  .brand__words { display: flex; flex-direction: column; line-height: 1; }
  .brand__initials { letter-spacing: -1px; }
  .brand__line { letter-spacing: 0.3px; text-transform: uppercase; }

  .card--front .brand { left: 92px; top: 130px; gap: 8px; }
  .card--front .brand__square { width: 30px; height: 30px; }
  .card--front .brand__initials { font-size: 38px; }
  .card--front .brand__line { font-size: 7.5px; margin-top: 2px; }

  .card--back .brand { left: 52px; top: 72px; gap: 14px; }
  .card--back .brand__square { width: 62px; height: 62px; }
  .card--back .brand__initials { font-size: 72px; }
  .card--back .brand__line { font-size: 11px; margin-top: 4px; }

  .contact {
    position: absolute;
    left: 50px;
    top: 205px;
    width: 220px;
    text-align: center;
    color: var(--text-dark);
    font-size: 16px;
  }
  .contact__icon { display: block; margin: 0 auto; }
  .contact__icon--phone { width: 14px; height: 16px; margin-bottom: 8px; }
  .contact__icon--mail { width: 16px; height: 12px; margin-top: 12px; margin-bottom: 9px; }

  .identity {
    position: absolute;
    left: 430px;
    top: 180px;
    width: 250px;
    text-align: center;
    color: var(--text-light);
  }
  .identity__name { font-size: 30px; font-weight: 600; line-height: 1.1; }
  .identity__title { font-size: 15px; margin-top: 4px; }
</style>
</head>
<body>

<section class="card card--front">
  <svg class="card__art" viewBox="0 0 543 324" preserveAspectRatio="none" aria-hidden="true">
    <rect width="543" height="324" fill="var(--card-grey)"/>
    <polygon points="0,62 383,62 368,80 368,246 383,262 0,262" fill="var(--card-white)"/>
    <polygon points="290,80 543,80 543,246 290,246 345,163" fill="var(--panel-dark)"/>
    <polygon points="272,80 290,80 345,163 290,246 272,246 327,163" fill="var(--card-grey)"/>
    <polygon points="236,80 272,80 327,163 272,246 236,246 291,163" fill="var(--accent-red)"/>
  </svg>

  <div class="brand">
    <span class="brand__square"></span>
    <span class="brand__words">
      <span class="brand__initials">KV</span>
      <span class="brand__line">Field Surveys</span>
    </span>
  </div>

  <div class="contact">
    <svg class="contact__icon contact__icon--phone" viewBox="0 0 14 16" aria-hidden="true">
      <path d="M3 1 L5.5 1 L6.5 4.5 L4.8 5.8 C5.6 8 6.8 9.8 8.8 11.2 L10.3 9.6 L13.2 11 L13 13.6 C12.6 14.6 11.6 15 10.6 14.8 C5.8 13.6 1.8 8.8 1 3.6 C0.9 2.2 1.8 1.2 3 1 Z" fill="var(--accent-red)"/>
    </svg>
    <div class="contact__phone">555 014 2290</div>
    <svg class="contact__icon contact__icon--mail" viewBox="0 0 16 12" aria-hidden="true">
      <rect width="16" height="12" fill="var(--accent-red)"/>
      <polyline points="0.5,0.8 8,7 15.5,0.8" fill="none" stroke="var(--card-white)" stroke-width="1.2"/>
    </svg>
    <div class="contact__email">hello@kvfield.com</div>
  </div>

  <div class="identity">
    <div class="identity__name">Your Name</div>
    <div class="identity__title">Title</div>
  </div>
</section>

<section class="card card--back">
  <svg class="card__art" viewBox="0 0 543 324" preserveAspectRatio="none" aria-hidden="true">
    <rect width="543" height="324" fill="var(--card-grey)"/>
    <polygon points="0,62 383,62 368,80 368,246 383,262 0,262" fill="var(--card-white)"/>
    <polygon points="290,80 543,80 543,246 290,246 345,163" fill="var(--panel-dark)"/>
    <polygon points="272,80 290,80 345,163 290,246 272,246 327,163" fill="var(--card-grey)"/>
    <polygon points="236,80 272,80 327,163 272,246 236,246 291,163" fill="var(--accent-red)"/>
  </svg>

  <div class="brand">
    <span class="brand__square"></span>
    <span class="brand__words">
      <span class="brand__initials">KV</span>
      <span class="brand__line">Field Surveys</span>
    </span>
  </div>
</section>

</body>
</html>
```